Bright Harbor Charity - helping the disadvantaged

I would like a new web site design for my charity BRIGHT HARBOR. The charity provides help for the disadvantaged. See current site
brightharbor.org.au for details. Please refer to the current site for information on the charity. The objectives of the charity are in the "about us" tab. You will also notice on the site that we provide information about events that we sponsor an area for this should be provided on the site.

Target Market(s)

We have two targets:
1. Individuals and Businesses that will donate money to the charity.
2. Individuals that are in need of support from the charity.

Industry/Entity Type

Charity

Requirements
Must have
• Ability for individuals to be able to understand the type of support we can provide.
Nice to have
• Our logo should be prominate on each pages
Should not have
• Should be use modern fonts

```html
<!DOCTYPE html>
<html lang="en">
<head>
<meta charset="utf-8">
<title>Bright Harbor – Assistance to People in Need</title>
<link href="https://fonts.googleapis.com/css2?family=Arimo:wght@400;700&family=Crimson+Text:wght@600;700&family=Rosarivo&display=swap" rel="stylesheet">
<style>
:root{
  --green:#2f7d1e;
  --green-dark:#1f5e12;
  --orange:#d98a17;
  --orange-light:#f1ab3c;
  --brown:#8a5a17;
  --text:#333;
  --footer-bg:#e3e8e5;
  --white:#fff;
  --line:#cfd6d2;
}
*{box-sizing:border-box;margin:0;padding:0}
html,body{width:1001px;height:1200px;overflow:hidden}
body{position:relative;background:var(--white);font-family:"Arimo",Arial,sans-serif;color:var(--text)}
.abs{position:absolute}

/* header */
.brand{left:111px;top:34px}
.brand-name{font-weight:700;font-size:26px;color:var(--green);letter-spacing:1px;line-height:1}
.brand-url{font-size:10px;color:var(--green);letter-spacing:2px;margin-top:7px}
.account{top:45px;display:flex;gap:8px;left:516px}
.account a{display:flex;align-items:center;gap:5px;height:22px;padding:0 10px;font-size:12px;color:var(--white);text-decoration:none;border-radius:2px}
.signin{background:var(--green)}
.register{background:var(--orange)}
.phone{left:697px;top:40px;display:flex;align-items:center;gap:8px;font-family:"Rosarivo",serif;font-size:24px;color:#222}

/* nav */
.nav{left:0;top:103px;width:1001px;height:44px;background:linear-gradient(#3f9128,var(--green-dark));display:flex;align-items:center;padding-left:111px}
.nav a{font-family:"Crimson Text",serif;font-weight:700;font-size:15px;color:var(--white);text-decoration:none;text-transform:uppercase;letter-spacing:.5px;padding:4px 14px;margin-right:9px}
.nav a.active{background:#f5efd9;color:#333;border:1px solid #c8b98a}

/* hero */
.hero{left:0;top:147px;width:1001px;height:813px;background:linear-gradient(180deg,#dfece7 0%,#eef4f1 40%,#f3f6f4 100%)}
.hero-art{left:0;top:147px;width:560px;height:360px;background:radial-gradient(ellipse at 45% 40%,#f4f0ec 0%,#d9e4df 50%,rgba(223,236,231,0) 75%)}
.hero-title{left:507px;top:202px;font-family:"Rosarivo",serif;font-weight:400;font-size:37px;line-height:42px;color:var(--green)}
.hero-sub{left:509px;top:302px;font-size:14px;line-height:17px;color:#555;width:380px}
.donate-btn{left:508px;top:353px;width:246px;height:54px;background:linear-gradient(var(--orange-light),var(--orange));border:1px solid #b46d0c;border-radius:3px;display:flex;align-items:center;justify-content:center;gap:10px;font-size:23px;color:var(--white);text-decoration:none}

/* content card */
.card{left:109px;top:453px;width:783px;height:469px;background:var(--white);border:1px solid #d6dcd8;box-shadow:0 0 6px rgba(0,0,0,.08)}
.section-title{font-size:25px;font-weight:400;color:var(--brown)}
.pager{left:834px;top:483px;display:flex;gap:3px}
.pager span{width:15px;height:15px;border-radius:50%;background:#bbb;display:flex;align-items:center;justify-content:center}
.pager span.on{background:#888}
.poster{left:144px;top:523px;width:263px;height:126px;border:4px solid var(--white);box-shadow:0 0 4px rgba(0,0,0,.25);background:linear-gradient(135deg,#fbe45a,#8fd1ee 60%,#6fb9e0)}
.news-title{left:436px;top:530px;font-size:16px;font-weight:400;color:#222}
.news-body{left:436px;top:559px;width:428px;font-size:10px;line-height:13px;color:#666}
.news-body em{font-style:normal;color:var(--brown)}
.news-meta{left:436px;top:626px;display:flex;align-items:center;font-size:10px;color:#444}
.more-btn{display:flex;align-items:center;gap:4px;height:21px;padding:0 10px;background:var(--green);color:var(--white);text-decoration:none;font-size:10px;margin-right:14px}
.news-meta .sep{margin:0 8px;width:1px;height:12px;background:#bbb}
.help{top:716px;width:226px}
.help-photo{height:123px;border:4px solid var(--white);box-shadow:0 0 4px rgba(0,0,0,.25)}
.help h3{font-size:14px;font-weight:700;color:#111;margin-top:12px}
.help p{font-size:11px;line-height:13px;color:#444;margin-top:3px;width:200px}
.help.wide p{width:232px}

/* footer */
.footer{left:0;top:960px;width:1001px;height:240px;background:var(--footer-bg)}
.foot-h{font-size:14px;font-weight:700;color:var(--green-dark)}
.foot-text{font-size:10px;line-height:14px;color:#555}
.news-input{left:698px;top:1022px;width:193px;height:26px;border:1px solid #aaa;background:var(--white);font-size:10px;color:#999;padding:0 8px;display:flex;align-items:center}
.sub-btn{left:699px;top:1056px;width:73px;height:20px;background:var(--green);color:var(--white);font-size:10px;display:flex;align-items:center;justify-content:center}
.links-bar{left:109px;top:1091px;width:783px;height:37px;background:var(--white);border:1px solid var(--line);display:flex;align-items:center;padding-left:14px;font-size:10px;color:#444}
.links-bar a{color:#444;text-decoration:none}
.links-bar i{font-style:normal;margin:0 5px;color:#888}
.social{position:absolute;right:10px;top:6px;display:flex;gap:5px}
.social span{width:24px;height:24px;border-radius:3px}
.copyright{left:109px;top:1142px;font-size:10px;color:#555}
.powered{color:#888}
</style>
</head>
<body>
<header>
  <div class="abs brand">
    <div class="brand-name">BRIGHT HARBOR</div>
    <div class="brand-url">w w w . brightharbor . org . au</div>
  </div>
  <div class="abs account">
    <a class="signin" href="#"><svg width="9" height="10" viewBox="0 0 9 10"><rect x="1" y="4" width="7" height="6" fill="#fff"/><path d="M2.5 4V3a2 2 0 0 1 4 0v1" stroke="#fff" fill="none"/></svg>Sign In</a>
    <a class="register" href="#"><svg width="10" height="10" viewBox="0 0 10 10"><circle cx="5" cy="3" r="2.3" fill="#fff"/><path d="M1 10a4 4 0 0 1 8 0z" fill="#fff"/></svg>Register</a>
  </div>
  <div class="abs phone">
    <svg width="26" height="26" viewBox="0 0 26 26"><circle cx="13" cy="13" r="11.5" fill="none" stroke="#2f7d1e" stroke-width="2"/><path d="M9 7.5l2.5 3-1.3 1.5a8 8 0 0 0 3.8 3.8l1.5-1.3 3 2.5-1.5 2c-5 0-10-5-10-10z" fill="#2f7d1e"/></svg>
    <span>+011 0400 1234</span>
  </div>
</header>

<nav class="abs nav">
  <a class="active" href="#">Home</a><a href="#">About</a><a href="#">Donate</a><a href="#">Apply</a><a href="#">Pledge</a><a href="#">Nominate</a><a href="#">Events</a><a href="#">Contact</a><a href="#">Director</a>
</nav>

<section class="abs hero"></section>
<div class="abs hero-art" role="img" aria-label="Soft illustration of a winged angel figure reaching toward the clouds"></div>
<h1 class="abs hero-title">Assistance to People<br>in Need in Australia</h1>
<p class="abs hero-sub">People in need includes orphaned children disabled people, people living under poverty...</p>
<a class="abs donate-btn" href="#">Make a Donation
  <svg width="24" height="24" viewBox="0 0 24 24"><circle cx="12" cy="12" r="10" fill="none" stroke="#fff" stroke-width="2"/><path d="M10 7l5 5-5 5" fill="none" stroke="#fff" stroke-width="2.5"/></svg>
</a>

<main class="abs card"></main>
<h2 class="abs section-title" style="left:146px;top:480px">Announcements</h2>
<div class="abs pager">
  <span><svg width="7" height="7" viewBox="0 0 7 7"><path d="M5 0.5L2 3.5 5 6.5" stroke="#fff" fill="none" stroke-width="1.5"/></svg></span>
  <span class="on"><svg width="7" height="7" viewBox="0 0 7 7"><path d="M2 0.5L5 3.5 2 6.5" stroke="#fff" fill="none" stroke-width="1.5"/></svg></span>
</div>
<div class="abs poster" role="img" aria-label="Harmony Day event poster for Saturday 24th March"></div>
<h3 class="abs news-title">Harmony Day Information Sheet &amp; Booking Form</h3>
<p class="abs news-body">Harmony Day is celebrated around Australia on 21st March each year. It's a day where all Australians celebrate our cultural diversity. The continuing message of Harmony Day is that <em>Everyone</em> Belongs, which means all Australians are a welcome part of our country, regardless <em>of their</em> background.</p>
<div class="abs news-meta">
  <a class="more-btn" href="#">+ Learn More</a>
  <span>24 March, 2012</span><span class="sep"></span><span>Posted in&nbsp; : &nbsp;News</span>
</div>

<h2 class="abs section-title" style="left:146px;top:677px">How can you help ?</h2>
<div class="abs help" style="left:144px">
  <div class="help-photo" role="img" aria-label="Photo of two smiling children" style="background:linear-gradient(135deg,#c9703a,#e8a35a 50%,#7a4a2a)"></div>
  <h3>Sponsor</h3><p>We can smile only because of you donation</p>
</div>
<div class="abs help" style="left:390px">
  <div class="help-photo" role="img" aria-label="Photo of a child at a classroom table" style="background:linear-gradient(135deg,#b7c7c9,#d8c4a6 50%,#8b6f58)"></div>
  <h3>Business Donate</h3><p>We can get eduction only because of you donation</p>
</div>
<div class="abs help wide" style="left:636px">
  <div class="help-photo" role="img" aria-label="Photo of a girl playing the piano" style="background:linear-gradient(135deg,#e6d7bf,#c9a77f 55%,#6d5a4a)"></div>
  <h3>Volunteer</h3><p>People can donate as our dreams depends on your donation only</p>
</div>

<footer class="abs footer"></footer>
<h4 class="abs foot-h" style="left:110px;top:995px">About Us</h4>
<p class="abs foot-text" style="left:110px;top:1021px;width:300px">Lorem Ipsum is simply dummy text of the printing and typesetting industry. Lorem Ipsum has been the industry's standard. dummy text ever since the 1500s, when an unknown.</p>
<h4 class="abs foot-h" style="left:467px;top:995px">Contact Us</h4>
<p class="abs foot-text" style="left:467px;top:1021px;line-height:19px">Email : info@brightharbor.org.au<br>Phone No. :&nbsp; (03) 9555 0142<br>Fax No. :&nbsp;&nbsp;&nbsp;&nbsp; (03) 9555 0199</p>
<h4 class="abs foot-h" style="left:696px;top:995px">Subscribe Newsletter</h4>
<div class="abs news-input">Enter Your Email Address</div>
<div class="abs sub-btn">Subscribe</div>
<div class="abs links-bar">
  <a href="#">Home</a><i>|</i><a href="#">About Us</a><i>|</i><a href="#">Donate</a><i>|</i><a href="#">Apply</a><i>|</i><a href="#">Pledge</a><i>|</i><a href="#">Nominate</a><i>|</i><a href="#">Events</a><i>|</i><a href="#">Contact Us</a><i>|</i><a href="#">Directors</a>
  <div class="social"><span style="background:#7fc6e0"></span><span style="background:#3b5b98"></span><span style="background:#1d7fb5"></span></div>
</div>
<p class="abs copyright">© Copyright 2012 BRIGHT HARBOR. All Rights Reserved. Terms &amp; Conditions | Privacy Policy | <span class="powered">Powered By : Northfield Studio</span></p>
</body>
</html>
```